Dalworth Construction Needs a Business Card

Our current business card is very bland, and since we have a new logo, we would like a new business card design to reflect our company. It can be a single-sided or two-sided card, but it is important that our contact information appears on the same side. I am attaching a copy of our old card and our new logo. If you need the logo in another format than the one I'm sending, please let me know. This is the information that we must have on our card, but not necessarily in any specific order:
1) Our logo
2) General Contractor
3) Grant Ellsworth, Owner
4) 482 Commerce Loop Road, Marlow Springs, Ohio 44920
5) Office: 555-418-7735
7) Fax: 555-418-7736
8) Cell: 555-609-4418
9) dalworthconstruction@qvx.net
10) dalworthconstruction.com (can be omitted if necessary)
Also, I will need files in a format that I can alter if any of the above information changes in the near future. Thank you in advance for your submissions!
Target Market(s)
Commercial and residential clients, architects, and subcontractors.
Industry/Entity Type
Business
Look and feel

```html
<!DOCTYPE html>
<html lang="en">
<head>
<meta charset="utf-8">
<title>Dalworth Construction — Business Card</title>
<link rel="stylesheet" href="https://fonts.googleapis.com/css2?family=Archivo:wght@500;700&family=Lato:wght@400;700&display=swap">
<style>
  :root {
    --backdrop: #2e2e2e;
    --card-black: #0b0409;
    --card-white: #ffffff;
    --brand-yellow: #fbbf24;
    --ink: #231f20;
    --text: #3a3a3a;
  }
  * { box-sizing: border-box; margin: 0; padding: 0; }
  html, body { width: 1200px; height: 900px; overflow: hidden; }
  body {
    background: var(--backdrop);
    font-family: "Lato", sans-serif;
    position: relative;
  }
  .card {
    position: absolute;
    top: 301px;
    width: 514px;
    height: 296px;
  }
  .card-back {
    left: 72px;
    background: var(--card-black);
    display: flex;
    align-items: center;
    justify-content: center;
    gap: 16px;
  }
  .back-mark {
    width: 34px;
    height: 34px;
    background: var(--brand-yellow);
  }
  .back-name {
    color: var(--brand-yellow);
    font-weight: 700;
    font-size: 30px;
    letter-spacing: 1px;
    text-transform: uppercase;
  }
  .card-front {
    left: 615px;
    background: var(--card-white);
  }
  .brand {
    position: absolute;
    left: 34px;
    top: 28px;
    display: flex;
    align-items: center;
    gap: 12px;
  }
  .brand-mark {
    width: 68px;
    height: 68px;
    background: var(--ink);
  }
  .brand-name {
    color: var(--ink);
    font-weight: 700;
    font-size: 28px;
    line-height: 1;
    text-transform: uppercase;
    letter-spacing: 0.5px;
  }
  .person {
    position: absolute;
    right: 35px;
    top: 128px;
    text-align: right;
    color: var(--text);
  }
  .person-name { font-weight: 700; font-size: 17px; line-height: 21px; }
  .person-title { font-size: 13px; line-height: 18px; }
  .address {
    position: absolute;
    left: 34px;
    top: 195px;
    font-size: 13px;
    line-height: 17px;
    color: var(--text);
    list-style: none;
  }
  .contacts {
    position: absolute;
    right: 35px;
    top: 178px;
    font-size: 13px;
    line-height: 17px;
    color: var(--text);
    list-style: none;
    text-align: right;
  }
  .contacts li { display: flex; justify-content: flex-end; align-items: center; gap: 5px; }
  .contacts svg { width: 10px; height: 10px; fill: var(--text); flex: none; }
  .band {
    position: absolute;
    left: 0; right: 0; bottom: 0;
    height: 42px;
    background: var(--brand-yellow);
    display: flex;
    align-items: center;
    justify-content: center;
    font-family: "Archivo", sans-serif;
    font-weight: 500;
    font-size: 17px;
    letter-spacing: 13.6px;
    color: var(--text);
    padding-left: 14px;
  }
</style>
</head>
<body>
  <section class="card card-back" aria-label="Card back">
    <span class="back-mark"></span>
    <span class="back-name">Dalworth Construction</span>
  </section>

  <section class="card card-front" aria-label="Card front">
    <div class="brand">
      <span class="brand-mark"></span>
      <span class="brand-name">Dalworth<br>Construction</span>
    </div>

    <div class="person">
      <p class="person-name">Grant Ellsworth</p>
      <p class="person-title">Owner</p>
    </div>

    <ul class="address">
      <li>482 Commerce Loop Road</li>
      <li>Marlow Springs, Ohio 44920</li>
      <li>www.dalworthconstruction.com</li>
    </ul>

    <ul class="contacts">
      <li>555-418-7735
        <svg viewBox="0 0 10 10" aria-label="Office"><path d="M2 0.5 L3.8 2.6 L2.8 3.6 Q4 6 6.4 7.2 L7.4 6.2 L9.5 8 L8.2 9.5 Q2 8.5 0.5 1.8 Z"/></svg>
      </li>
      <li>555-418-7736
        <svg viewBox="0 0 10 10" aria-label="Fax"><rect x="2.5" y="0.5" width="5" height="3"/><rect x="0.5" y="3.5" width="9" height="4" rx="1"/><rect x="2.5" y="7" width="5" height="2.5"/></svg>
      </li>
      <li>555-609-4418
        <svg viewBox="0 0 10 10" aria-label="Cell"><path d="M3 0.5 H7 V9.5 H3 Z M3.8 1.5 V7.8 H6.2 V1.5 Z"/></svg>
      </li>
      <li>dalworthconstruction@qvx.net
        <svg viewBox="0 0 10 10" aria-label="Email"><path d="M0.5 2 H9.5 V8 H0.5 Z"/><path d="M1.2 2.6 L5 5.4 L8.8 2.6" stroke="#fff" stroke-width="0.8" fill="none"/></svg>
      </li>
    </ul>

    <div class="band">GENERAL CONTRACTOR</div>
  </section>
</body>
</html>
```